Business Card Design

Marla Quibbet
Artist of Contemporary/Modern/Representational Art
Contact: 0457219308
Please include my web site (thanks)! http://www.artvault913.com.au/marla-quibbet
And
Email: marlaquibbet@fernpost.example

Target Market(s)

Modern professional People who know what they like in modern contemporary art and have the means to purchase it.

Industry/Entity Type

Business

Contact Information for Business Card

Marla Quibbet
Contact: 0457219308

Font styles to use
Sans Serif

Requirements
Must have
• Simplicity & to the point
Keep the font modern/ contemporary
Nice to have
• A portrait of me and one piece of work on the business card (one on each side).
Should not have
• I'm not into butterflies.
No feminine style swirls
Nor I like swirls that look like tatoos

```html
<!DOCTYPE html>
<html lang="en">
<head>
<meta charset="utf-8">
<title>Marla Quibbet – Business Card</title>
<link rel="stylesheet" href="https://fonts.googleapis.com/css2?family=Arimo:wght@400;700&display=swap">
<style>
  :root {
    --page: #ffffff;
    --card-dark: #2c2c2c;
    --card-dark-edge: #232323;
    --olive: #b9b57c;
    --olive-text: #c9c48a;
    --white: #ffffff;
    --soft-white: #e9e9e9;
    --icon: #bdbdbd;
    --frame: #d8d2b6;
  }
  * { margin: 0; padding: 0; box-sizing: border-box; }
  html, body {
    width: 900px; height: 1200px; overflow: hidden;
    background: var(--page);
    font-family: "Arimo", Arial, sans-serif;
  }
  .canvas { position: relative; width: 900px; height: 1200px; }

  /* Front face */
  .card-front {
    position: absolute; left: 39px; top: 42px; width: 825px; height: 519px;
    background: radial-gradient(ellipse at 60% 40%, #343434 0%, var(--card-dark) 55%, var(--card-dark-edge) 100%);
    overflow: hidden;
  }
  .portrait {
    position: absolute; left: 102px; top: 87px; width: 140px; height: 186px;
    border: 3px solid var(--frame);
    background: linear-gradient(160deg, #8a6a55 0%, #b89277 40%, #d8b79a 65%, #6d4f3e 100%);
  }
  .accent-band {
    position: absolute; left: 102px; top: 273px; width: 140px; bottom: 0;
    background: var(--olive);
  }
  .identity { position: absolute; left: 310px; top: 180px; }
  .name {
    color: var(--white); font-weight: 700; font-size: 26px; letter-spacing: 0.3px;
  }
  .tagline {
    margin-top: 6px; color: var(--olive-text); font-size: 22px; line-height: 30px;
  }
  .contacts { position: absolute; left: 312px; top: 352px; list-style: none; }
  .contact {
    display: flex; align-items: center; gap: 16px;
    color: var(--soft-white); font-size: 23px; height: 34px;
  }
  .contact svg { width: 18px; height: 18px; flex: none; }

  /* Back face */
  .card-back {
    position: absolute; left: 36px; top: 636px; width: 828px; height: 504px;
    display: flex; gap: 6px; background: var(--page);
  }
  .artwork { height: 100%; }
  .artwork-houses {
    width: 408px;
    background: linear-gradient(180deg, #6d8fb0 0%, #c9a347 30%, #b8432f 55%, #d3c24a 70%, #7a5a48 100%);
  }
  .artwork-city {
    flex: 1;
    background: radial-gradient(ellipse at 55% 45%, #4f7fa6 0%, #c7583c 40%, #d7b277 62%, #3c2f2a 100%);
  }
</style>
</head>
<body>
<main class="canvas">
  <section class="card-front" aria-label="Business card front">
    <div class="portrait" role="img" aria-label="Portrait photograph of the artist"></div>
    <div class="accent-band"></div>
    <div class="identity">
      <h1 class="name">Marla QUIBBET</h1>
      <p class="tagline">Artist of Contemporary<br>Modern | Representational Art</p>
    </div>
    <ul class="contacts">
      <li class="contact">
        <svg viewBox="0 0 20 20" aria-hidden="true"><rect x="2" y="4.5" width="16" height="11" fill="none" stroke="var(--icon)" stroke-width="1.6"/><path d="M2 4.5 L10 11 L18 4.5" fill="none" stroke="var(--icon)" stroke-width="1.6"/></svg>
        <span>marlaquibbet@fernpost.example</span>
      </li>
      <li class="contact">
        <svg viewBox="0 0 20 20" aria-hidden="true"><path d="M5 2.5 L8 2.5 L9 6.5 L7 8 Q8.5 11.5 12 13 L13.5 11 L17.5 12 L17.5 15 Q17 17.5 14.5 17.5 Q3 16 2.5 5.5 Q2.5 3 5 2.5 Z" fill="var(--icon)"/></svg>
        <span>0457219308</span>
      </li>
      <li class="contact">
        <svg viewBox="0 0 20 20" aria-hidden="true"><circle cx="10" cy="10" r="7.5" fill="none" stroke="var(--icon)" stroke-width="1.6"/><ellipse cx="10" cy="10" rx="3.2" ry="7.5" fill="none" stroke="var(--icon)" stroke-width="1.4"/><path d="M2.5 10 H17.5" stroke="var(--icon)" stroke-width="1.4"/></svg>
        <span>www.artvault913.com.au/marla-quibbet</span>
      </li>
    </ul>
  </section>

  <section class="card-back" aria-label="Business card back">
    <div class="artwork artwork-houses" role="img" aria-label="Painting of colourful tall narrow townhouses along a waterfront"></div>
    <div class="artwork artwork-city" role="img" aria-label="Painting of an old city island with red roofs and spires seen from above"></div>
  </section>
</main>
</body>
</html>
```